Landscaping flier 2024

Create a 1 page flier for landscaping services
1. Must be completed in Adobe Photoshop
2. Size 8.5" x 11" (portrait layout)
3. Include logo
4. Text to include:
2024 Gravesite Landscaping Packages
info@maplecrestmemorial.example
(201) 555-0148
maplecrestmemorial.example
5. Use chart text for the content. DO NOT COPY THE CHART DESIGN/FORMAT. Use the chart for the text you need only.
6. Use "Pricing cards as format for laying out the chart". Open to other ideas as well.
**Use the example of chart design (handwritten) to base your design off of.
7. Photos
-include before and after care photos

```html
<!DOCTYPE html>
<html lang="en">
<head>
<meta charset="utf-8">
<title>2024 Gravesite Landscaping Packages</title>
<link href="https://fonts.googleapis.com/css2?family=Open+Sans:wght@400;600;700;800&family=Montserrat:wght@800&display=swap" rel="stylesheet">
<style>
:root{
  --page:#f0eff0;
  --maroon:#7a2232;
  --maroon-soft:#9a4a58;
  --ink:#222;
  --band:#4a4a4a;
  --line:#e4e4e4;
  --check:#5c9b2c;
  --cross:#e5232b;
  --ribbon:#e8202a;
  --footer-text:#555;
}
*{margin:0;padding:0;box-sizing:border-box}
html,body{width:927px;height:1200px;overflow:hidden;background:var(--page)}
body{position:relative;font-family:"Open Sans",Arial,sans-serif;color:var(--ink)}
.brand{position:absolute;top:30px;left:0;width:927px;display:flex;justify-content:center;align-items:center;gap:14px}
.brand-name{font-family:"Open Sans",Arial,sans-serif;font-weight:600;font-size:24px;letter-spacing:1px;color:var(--maroon);text-transform:uppercase}
.brand-mark{width:44px;height:44px;border-radius:50%;border:2px solid var(--maroon)}
.photos{position:absolute;top:102px;left:0;width:927px;height:347px;display:flex}
.photo{position:relative;flex:1;height:100%}
.photo-before{background:linear-gradient(180deg,#9aa49c 0%,#6e9a48 35%,#5f8e32 65%,#4f7a2a 100%)}
.photo-after{background:linear-gradient(180deg,#a3aba6 0%,#6f9a4a 35%,#5e8c36 65%,#54803a 100%)}
.photo-label{position:absolute;bottom:14px;font-weight:800;font-size:23px;color:#fff;text-shadow:0 1px 3px rgba(0,0,0,.5)}
.photo-before .photo-label{left:61px}
.photo-after .photo-label{right:57px}
.title{position:absolute;top:474px;left:0;width:927px;text-align:center;font-family:"Montserrat",Arial,sans-serif;font-weight:800;font-size:29px;letter-spacing:2.6px;color:var(--maroon)}
.card{position:absolute;top:526px;background:#fff;box-shadow:0 1px 5px rgba(0,0,0,.18);height:594px;display:flex;flex-direction:column}
.col-services{left:61px;width:223px}
.col-seasonal{left:299px;width:179px}
.col-basic{left:493px;width:179px}
.col-perpetual{left:687px;width:179px;overflow:hidden}
.card-head{height:111px;display:flex;flex-direction:column;align-items:center;justify-content:center;text-align:center;padding:0 4px}
.plan-name{font-weight:700;font-size:20px;line-height:21px;color:var(--maroon)}
.plan-desc{font-weight:600;font-size:9.5px;line-height:12px;margin-top:7px;color:var(--ink)}
.services-title{font-weight:700;font-size:21px;line-height:26px;color:var(--maroon)}
.band{height:67px;background:var(--band);color:#fff;display:flex;align-items:center;justify-content:center;text-align:center;font-weight:600;font-size:9.5px;line-height:12.3px;padding:0 6px}
.col-services .band{justify-content:flex-start;text-align:left;font-size:16.5px;line-height:20px;padding-left:12px;margin-left:-1px;width:224px}
.row{display:flex;align-items:center;justify-content:center;border-bottom:1px solid var(--line)}
.row:nth-of-type(8){border-bottom:none}
.r1{height:56px}.r2{height:54px}.r3{height:52px}.r4{height:54px}.r5{height:51px}.r6{height:51px}
.col-services .row{justify-content:flex-start;padding-left:12px;font-weight:600;font-size:16.5px;line-height:20px;text-transform:uppercase}
.icon{width:24px;height:24px}
.price{flex:1;background:var(--maroon);color:#fff;display:flex;flex-direction:column;align-items:center;justify-content:center;text-align:center}
.price-small{font-weight:700;font-size:8.5px}
.price-big{font-weight:800;font-size:47px;line-height:52px}
.price-note{font-style:italic;font-weight:600;font-size:8px}
.terms{display:flex;margin-bottom:6px}
.term{padding:0 4px;font-weight:800;font-size:13px;line-height:16px}
.term+.term{border-left:1px solid #fff}
.valid{flex:1;display:flex;flex-direction:column;align-items:flex-end;justify-content:center;padding-right:13px;padding-bottom:10px;color:var(--maroon-soft);font-size:13.5px;line-height:18px}
.ribbon{position:absolute;top:0;left:0;width:66px;height:66px}
.contact{position:absolute;top:1147px;left:0;width:927px;text-align:center;font-weight:600;font-size:18px;color:var(--footer-text)}
.contact .sep{margin:0 12px;font-weight:400}
.base-bar{position:absolute;bottom:0;left:0;width:927px;height:13px;background:var(--band)}
</style>
</head>
<body>
<svg width="0" height="0" style="position:absolute">
  <symbol id="tick" viewBox="0 0 24 24"><path d="M3 12.5l6 6L21 6" fill="none" stroke="#5c9b2c" stroke-width="3.2" stroke-linecap="round" stroke-linejoin="round"/></symbol>
  <symbol id="cross" viewBox="0 0 24 24"><path d="M5 5l14 14M19 5L5 19" fill="none" stroke="#e5232b" stroke-width="3.4" stroke-linecap="round"/></symbol>
</svg>

<header class="brand">
  <span class="brand-name">Maplecrest</span>
  <span class="brand-mark"></span>
  <span class="brand-name">Memorial</span>
</header>

<section class="photos">
  <div class="photo photo-before" role="img" aria-label="Overgrown gravesite with weeds in front of a granite headstone before landscaping care"><span class="photo-label">BEFORE</span></div>
  <div class="photo photo-after" role="img" aria-label="Same gravesite after care with a neatly trimmed boxwood bed and clean headstone"><span class="photo-label">AFTER</span></div>
</section>

<h1 class="title">2024 GRAVESITE LANDSCAPING PACKAGES</h1>

<div class="card col-services">
  <div class="card-head"><div class="services-title">SERVICES<br>OFFERED</div></div>
  <div class="band">WEEDING &amp; TRIMMING<br>ON YOUR GRAVESITE</div>
  <div class="row r1">Payment ensures<br>grave care forever</div>
  <div class="row r2">Monument<br>leveling</div>
  <div class="row r3">Monument<br>cleaning</div>
  <div class="row r4">Full bed of<br>boxwood shrubs</div>
  <div class="row r5">Replacement<br>of shrubs</div>
  <div class="row r6">Trust<br>certificate</div>
  <div class="valid"><span>VALID THROGH</span><span>10/31/2024</span></div>
</div>

<div class="card col-seasonal">
  <div class="card-head"><div class="plan-name">SEASONAL<br>CARE</div><div class="plan-desc">SEASONAL<br>LANDSCAPING GRAVE CARE</div></div>
  <div class="band">APPROXIMATELY<br>EVERY 7 WEEKS DURING THE GROWING SEASON: MID-APRIL THROUGH MID-OCTOBER</div>
  <div class="row r1"><svg class="icon"><use href="#cross"/></svg></div>
  <div class="row r2"><svg class="icon"><use href="#cross"/></svg></div>
  <div class="row r3"><svg class="icon"><use href="#cross"/></svg></div>
  <div class="row r4"><svg class="icon"><use href="#cross"/></svg></div>
  <div class="row r5"><svg class="icon"><use href="#cross"/></svg></div>
  <div class="row r6"><svg class="icon"><use href="#cross"/></svg></div>
  <div class="price">
    <div class="terms">
      <div class="term">03<br>YEARS<br>$396</div>
      <div class="term">02<br>YEARS<br>$264</div>
      <div class="term">01<br>YEAR<br>$132</div>
    </div>
    <div class="price-note">Multi-years payment locks<br>in current rates.</div>
  </div>
</div>

<div class="card col-basic">
  <div class="card-head"><div class="plan-name">BASIC CARE<br>ENDOWMENT</div><div class="plan-desc">LANDSCAPING CARE FOREVER FOR GRAVES WITH NO PLANTINGS.</div></div>
  <div class="band">2 TIMES PER YEAR:<br>MID-MAY &amp; MID-SEPTEMBER</div>
  <div class="row r1"><svg class="icon"><use href="#tick"/></svg></div>
  <div class="row r2"><svg class="icon"><use href="#tick"/></svg></div>
  <div class="row r3"><svg class="icon"><use href="#cross"/></svg></div>
  <div class="row r4"><svg class="icon"><use href="#cross"/></svg></div>
  <div class="row r5"><svg class="icon"><use href="#cross"/></svg></div>
  <div class="row r6"><svg class="icon"><use href="#cross"/></svg></div>
  <div class="price">
    <div class="price-small">12 monthly payment of</div>
    <div class="price-big">$287</div>
    <div class="price-note">Call for single payment discount</div>
  </div>
</div>

<div class="card col-perpetual">
  <svg class="ribbon" viewBox="0 0 66 66" aria-label="Most popular">
    <polygon points="0,26 26,0 66,0 0,66" fill="#e8202a"/>
    <text x="20" y="20" transform="rotate(-45 20 20)" text-anchor="middle" font-family="Open Sans, sans-serif" font-weight="800" font-size="8.5" fill="#fff">MOST</text>
    <text x="27" y="27" transform="rotate(-45 27 27)" text-anchor="middle" font-family="Open Sans, sans-serif" font-weight="800" font-size="8.5" fill="#fff">POPULAR</text>
  </svg>
  <div class="card-head" style="align-items:flex-end;text-align:right;padding-right:14px"><div class="plan-name">PERPETUAL<br>CARE<br>ENDOWMENT</div><div class="plan-desc" style="text-align:center;margin-top:4px">LANDSCAPING. CARE FOREVER FOR GRAVES WITH PLANTINGS.</div></div>
  <div class="band">APPROXIMATELY<br>EVERY 7 WEEKS DURING THE GROWING SEASON: MID-APRIL THROUGH MID-OCTOBER</div>
  <div class="row r1"><svg class="icon"><use href="#tick"/></svg></div>
  <div class="row r2"><svg class="icon"><use href="#tick"/></svg></div>
  <div class="row r3"><svg class="icon"><use href="#tick"/></svg></div>
  <div class="row r4"><svg class="icon"><use href="#tick"/></svg></div>
  <div class="row r5"><svg class="icon"><use href="#tick"/></svg></div>
  <div class="row r6"><svg class="icon"><use href="#tick"/></svg></div>
  <div class="price">
    <div class="price-small">12 monthly payment of</div>
    <div class="price-big">$351</div>
    <div class="price-note">Call for single payment discount</div>
  </div>
</div>

<footer class="contact">info@maplecrestmemorial.example<span class="sep">|</span>(201) 555-0148<span class="sep">|</span>maplecrestmemorial.example</footer>
<div class="base-bar"></div>
</body>
</html>
```